Personal Training Studio business cards

Black logo on front. Also need: Carlyse Brondway Master Trainer, Phone: 0498315627 on the front.
On the back want the white logo and also want 10 stars or similar that can be stamped when attended Studio. The 10th start to have "Free" written under it.
Also want a line to write an appointment date and time on it.

```html
<!DOCTYPE html>
<html lang="en">
<head>
<meta charset="utf-8">
<title>Peak Form – Business Card</title>
<link href="https://fonts.googleapis.com/css2?family=Roboto:wght@400;500;700&family=Roboto+Condensed:wght@700&display=swap" rel="stylesheet">
<style>
  :root {
    --backdrop: #5f5f5f;
    --card-dark: #000000;
    --card-light: #ffffff;
    --brand-purple: #6a4ea3;
    --line-purple: #9a86cf;
    --brand-green: #8dc63f;
    --text-light: #ffffff;
    --text-dark: #111111;
    --free-grey: #555555;
  }
  * { box-sizing: border-box; margin: 0; padding: 0; }
  html, body {
    width: 1200px; height: 1200px; overflow: hidden;
    background: var(--backdrop);
    font-family: "Roboto", Arial, sans-serif;
  }
  .sheet {
    position: relative; width: 1200px; height: 1200px;
  }
  .card {
    position: absolute; left: 150px; width: 900px; height: 522px;
    overflow: hidden;
  }
  .card--front { top: 58px; background: var(--card-dark); }
  .card--back  { top: 620px; background: var(--card-light); }

  /* Front */
  .brand {
    position: absolute; left: 56px; top: 222px; width: 360px;
    display: flex; align-items: center; gap: 14px;
  }
  .brand__dot {
    width: 26px; height: 26px; border-radius: 50%;
    background: var(--brand-green); flex: none;
  }
  .brand__name {
    font-weight: 700; font-size: 54px; letter-spacing: 1px;
    color: var(--brand-purple); line-height: 1; white-space: nowrap;
  }
  .divider {
    position: absolute; left: 449px; top: 186px; width: 2px; height: 149px;
    background: #9a9a9a;
  }
  .contact {
    position: absolute; left: 495px; top: 192px;
  }
  .contact__name {
    font-weight: 500; font-size: 42px; color: var(--text-light); line-height: 1.1;
  }
  .contact__role {
    font-size: 28px; color: var(--brand-green); margin-top: 8px;
  }
  .contact__phone {
    display: flex; align-items: center; gap: 8px;
    font-size: 28px; color: var(--text-light); margin-top: 14px; letter-spacing: 1px;
  }
  .contact__phone svg { width: 18px; height: 26px; }

  /* Back */
  .loyalty__title {
    position: absolute; top: 30px; left: 0; width: 100%; text-align: center;
    font-family: "Roboto Condensed", "Arial Narrow", sans-serif;
    font-weight: 700; font-size: 37px; letter-spacing: 1px; color: var(--text-dark);
  }
  .stamp {
    position: absolute; width: 132px; height: 160px;
  }
  .stamp__num {
    position: absolute; left: 0; top: 0;
    width: 26px; height: 26px; border-radius: 50%;
    background: var(--brand-purple); color: #fff;
    font-size: 15px; font-weight: 700;
    display: flex; align-items: center; justify-content: center;
  }
  .stamp__star {
    position: absolute; left: 14px; top: 4px; width: 104px; height: 104px;
  }
  .stamp__free {
    position: absolute; left: 0; top: 48px; width: 132px; text-align: center;
    font-family: "Roboto Condensed", "Arial Narrow", sans-serif;
    font-weight: 700; font-size: 15px; color: var(--free-grey);
  }
  .stamp__line {
    position: absolute; left: 0; top: 146px; width: 132px; height: 2px;
    background: var(--line-purple);
  }
</style>
</head>
<body>
<svg width="0" height="0" style="position:absolute">
  <defs>
    <symbol id="star-outline" viewBox="0 0 100 100">
      <polygon points="50,4 61.8,35.8 95.6,37.2 69,58.2 78.2,90.8 50,72 21.8,90.8 31,58.2 4.4,37.2 38.2,35.8"
               fill="none" stroke="#8dc63f" stroke-width="2" stroke-linejoin="miter"/>
    </symbol>
  </defs>
</svg>

<main class="sheet">
  <section class="card card--front">
    <div class="brand">
      <span class="brand__dot"></span>
      <span class="brand__name">PEAK FORM</span>
    </div>
    <div class="divider"></div>
    <div class="contact">
      <p class="contact__name">Carlyse Brondway</p>
      <p class="contact__role">Master Trainer</p>
      <p class="contact__phone">
        <svg viewBox="0 0 18 26" aria-hidden="true">
          <rect x="2" y="1.5" width="14" height="23" rx="2" fill="none" stroke="#fff" stroke-width="2.5"/>
          <rect x="6" y="19" width="6" height="2" fill="#fff"/>
        </svg>
        0498315627
      </p>
    </div>
  </section>

  <section class="card card--back">
    <h2 class="loyalty__title">Appointment</h2>

    <div class="stamp" style="left:35px;top:139px"><span class="stamp__num">1</span><svg class="stamp__star"><use href="#star-outline"/></svg><span class="stamp__line"></span></div>
    <div class="stamp" style="left:211px;top:139px"><span class="stamp__num">2</span><svg class="stamp__star"><use href="#star-outline"/></svg><span class="stamp__line"></span></div>
    <div class="stamp" style="left:388px;top:139px"><span class="stamp__num">3</span><svg class="stamp__star"><use href="#star-outline"/></svg><span class="stamp__line"></span></div>
    <div class="stamp" style="left:564px;top:139px"><span class="stamp__num">4</span><svg class="stamp__star"><use href="#star-outline"/></svg><span class="stamp__line"></span></div>
    <div class="stamp" style="left:741px;top:139px"><span class="stamp__num">5</span><svg class="stamp__star"><use href="#star-outline"/></svg><span class="stamp__line"></span></div>

    <div class="stamp" style="left:35px;top:340px"><span class="stamp__num">6</span><svg class="stamp__star"><use href="#star-outline"/></svg><span class="stamp__line"></span></div>
    <div class="stamp" style="left:211px;top:340px"><span class="stamp__num">7</span><svg class="stamp__star"><use href="#star-outline"/></svg><span class="stamp__line"></span></div>
    <div class="stamp" style="left:388px;top:340px"><span class="stamp__num">8</span><svg class="stamp__star"><use href="#star-outline"/></svg><span class="stamp__line"></span></div>
    <div class="stamp" style="left:564px;top:340px"><span class="stamp__num">9</span><svg class="stamp__star"><use href="#star-outline"/></svg><span class="stamp__line"></span></div>
    <div class="stamp" style="left:741px;top:340px"><span class="stamp__num" style="font-size:12px">10</span><svg class="stamp__star"><use href="#star-outline"/></svg><span class="stamp__free">FREE</span><span class="stamp__line"></span></div>
  </section>
</main>
</body>
</html>
```